Podcast Cover Art for Fast Growing Show (Ill include a gracious tip!)

This artwork is for "The Steadfast Fellow Show." The podcast is for men, and it's all about self-improvement, confidence, success, money, women and masculinity. It's for the guy who wants to improve himself. I'd like for my picture to be included — in black and white — and I want the text to read: "The Steadfast Fellow Show" and somewhere in there it'll say: "with Dale Prowen." I'm open to color schemes. The podcast is a little edgy so I'd like for that to be represented in the design. Thank you! (((Here's the podcast page if you wanna check it out: http://steadfastfellowshow.castorbit.net/)))

Target Market(s)

Men who want to attract women and improve their lives!

Font styles to use
Serif

Colors

Designer to choose colors to be used in the design.

Requirements
Must have
• My image in it (in black and white) and the two titles: "The Steadfast Fellow Show" and "with Dale Prowen"
Nice to have
• My logo in it somehow (which is the arrow looking logo attached below). I've also found that my image looks best in black and white and with a circular type cut out (although I'm open to different design ideas). I've attached my logo with a circular cut out below so you can see what I'm talking about.
Should not have
• Flowers. Teddy bears. ice cream.

```html
<!DOCTYPE html>
<html lang="en">
<head>
<meta charset="utf-8">
<title>The Steadfast Fellow Show – Cover Art</title>
<link href="https://fonts.googleapis.com/css2?family=Kanit:ital,wght@1,900&family=Oswald:wght@600&display=swap" rel="stylesheet">
<style>
  :root {
    --orange-deep: #ff8a00;
    --orange-light: #ffc20e;
    --ink: #000000;
    --title-top: #ffffff;
    --title-bottom: #cfcfcf;
    --accent: #ffb400;
    --outline: #ffffff;
    --photo-light: #8a8a8a;
    --photo-dark: #1a1a1a;
  }
  html, body { margin: 0; padding: 0; overflow: hidden; background: var(--ink); }
  .cover {
    position: relative;
    width: 1200px;
    height: 1000px;
    overflow: hidden;
    background: var(--ink);
  }
  .cover__backdrop { position: absolute; inset: 0; }
  .cover__title {
    position: absolute;
    left: 0;
    top: 100px;
    width: 780px;
    margin: 0;
    text-align: center;
    font-family: "Kanit", sans-serif;
    font-style: italic;
    font-weight: 900;
    font-size: 100px;
    line-height: 92px;
    letter-spacing: -1px;
    text-transform: uppercase;
    white-space: nowrap;
    background: linear-gradient(180deg, var(--title-top) 45%, var(--title-bottom) 100%);
    -webkit-background-clip: text;
    background-clip: text;
    color: transparent;
    filter: drop-shadow(3px 4px 3px rgba(0,0,0,0.35));
  }
  .cover__title span { display: block; }
  .cover__host-band {
    position: absolute;
    left: 0;
    top: 415px;
    width: 700px;
    height: 63px;
    background: var(--ink);
    display: flex;
    align-items: center;
    justify-content: center;
  }
  .cover__host {
    margin: 0 0 0 40px;
    font-family: "Oswald", sans-serif;
    font-weight: 600;
    font-size: 40px;
    letter-spacing: 0.5px;
    text-transform: uppercase;
    white-space: nowrap;
    color: var(--accent);
  }
  .cover__portrait { position: absolute; inset: 0; }
</style>
</head>
<body>
<main class="cover">
  <svg class="cover__backdrop" width="1200" height="1000" viewBox="0 0 1200 1000" aria-hidden="true">
    <defs>
      <linearGradient id="orangeSweep" x1="0" y1="0" x2="1" y2="0">
        <stop offset="0" stop-color="var(--orange-deep)"/>
        <stop offset="1" stop-color="var(--orange-light)"/>
      </linearGradient>
    </defs>
    <path fill="url(#orangeSweep)"
      d="M0 0 H965 L930 40 L900 150 L880 260 L860 330 L820 380 L780 400 L740 415 L0 415 Z"/>
    <path fill="url(#orangeSweep)"
      d="M0 478 H700 L705 500 L690 540 L670 560 L640 600 L620 590 L600 620 L570 605 L540 630 L510 612
         L480 640 L455 620 L430 650 L400 625 L370 645 L340 618 L310 640 L285 615 L255 632 L230 600
         L205 620 L180 590 L150 605 L120 580 L95 600 L70 575 L40 590 L20 570 L0 585 Z"/>
  </svg>

  <h1 class="cover__title">
    <span>The</span>
    <span>Steadfast</span>
    <span>Fellow Show</span>
  </h1>

  <div class="cover__host-band">
    <p class="cover__host">With Dale Prowen</p>
  </div>

  <svg class="cover__portrait" width="1200" height="1000" viewBox="0 0 1200 1000"
       role="img" aria-label="Black and white portrait of host Dale Prowen, hands steepled in front of his chin">
    <defs>
      <linearGradient id="portraitTone" x1="0" y1="0" x2="0" y2="1">
        <stop offset="0" stop-color="var(--photo-light)"/>
        <stop offset="0.55" stop-color="#4a4a4a"/>
        <stop offset="1" stop-color="var(--photo-dark)"/>
      </linearGradient>
    </defs>
    <path fill="url(#portraitTone)" stroke="var(--outline)" stroke-width="5"
      d="M830 160 C840 60 930 15 1030 20 C1130 25 1190 90 1180 200 L1175 320
         C1170 420 1150 480 1110 510 L1200 540 V1000 H345 L420 900 L520 820
         L600 760 L700 700 L760 540 C770 480 790 420 800 330 C790 280 790 220 830 160 Z"/>
  </svg>
</main>
</body>
</html>
```